Vela Stewardship Business Card design

We need a creative business card design for our hospitality management company
We need the following information:
Our business Logo: Vela Stewardship
Name: Mara Dobrinsky
Phone number: 0458 317 642
Email: mara@velastewardship.com.au
Address: 214/53 Penrose Street, Port Ellery 3215
Web: www.velastewardship.com.au
I need the design to be a working file so that I can insert the names and numbers of the other staff members of our business.
The cards need to be 90 x 40mm
Thanks
Industry/Entity Type
Hospitality
Look and feel

```html
<!DOCTYPE html>
<html lang="en">
<head>
<meta charset="utf-8">
<title>Vela Stewardship Business Card</title>
<link rel="stylesheet" href="https://fonts.googleapis.com/css2?family=Saira:wght@400;600&display=swap">
<style>
  :root {
    --page-bg: #d9d6d0;
    --blue-light: #4a9fd8;
    --blue-mid: #1f6aa5;
    --blue-deep: #0c3a63;
    --navy: #06223d;
    --panel-dark: #111316;
    --panel-edge: #2a86c9;
    --text-white: #ffffff;
    --text-soft: #e4eef7;
    --text-accent: #63b6ee;
    --brand-blue: #2f86cc;
  }
  * { margin: 0; padding: 0; box-sizing: border-box; }
  html, body {
    width: 1200px; height: 534px; overflow: hidden;
    background: var(--page-bg);
    font-family: "Saira", sans-serif;
  }
  .canvas { position: relative; width: 1200px; height: 534px; }
  .card {
    position: absolute; top: 152px; width: 517px; height: 228px; overflow: hidden;
  }
  .card--front {
    left: 62px;
    background: linear-gradient(160deg, var(--blue-light) 0%, var(--blue-mid) 40%, var(--blue-deep) 100%);
  }
  .card--back {
    left: 622px;
    background:
      linear-gradient(200deg, rgba(120,190,240,0.35) 0%, rgba(120,190,240,0) 30%),
      linear-gradient(180deg, var(--blue-mid) 0%, var(--blue-deep) 45%, var(--navy) 100%);
  }
  .front-frame {
    position: absolute; left: 26px; top: 25px; right: 25px; bottom: 23px;
    background: var(--panel-dark);
    border: 3px solid var(--panel-edge);
    box-shadow: inset 0 0 14px rgba(0,0,0,0.8);
  }
  .front-square {
    position: absolute; left: 50%; top: 31px; width: 66px; height: 64px;
    transform: translateX(-50%);
    border: 4px solid var(--brand-blue);
  }
  .front-brand {
    position: absolute; left: 0; right: 0; top: 117px;
    text-align: center;
    font-weight: 600; font-size: 21px; line-height: 26px; letter-spacing: 0.2px;
    color: var(--brand-blue); text-transform: uppercase;
  }
  .back-panel {
    position: absolute; left: 27px; top: 0; width: 188px; height: 228px;
    background: var(--panel-dark);
    border-top: 25px solid var(--blue-mid);
    border-bottom: 23px solid var(--blue-deep);
    box-shadow: inset 0 3px 0 var(--panel-edge);
  }
  .back-info { position: absolute; left: 258px; top: 0; right: 0; bottom: 0; color: var(--text-soft); }
  .brand-row { position: absolute; top: 33px; left: 0; display: flex; align-items: center; gap: 9px; }
  .brand-square { width: 37px; height: 38px; border: 3px solid var(--text-white); }
  .brand-name {
    font-weight: 600; font-size: 14.5px; color: var(--text-white);
    text-transform: uppercase; letter-spacing: 0;
  }
  .person-name {
    position: absolute; top: 102px; left: 0;
    font-size: 14px; color: var(--text-accent); text-transform: uppercase; letter-spacing: 0.4px;
  }
  .address { position: absolute; top: 127px; left: 0; font-size: 12px; line-height: 14px; }
  .contacts { position: absolute; top: 166px; left: 0; list-style: none; font-size: 12px; line-height: 14px; }
  .contacts li { display: flex; align-items: center; gap: 6px; }
  .contacts svg { width: 10px; height: 10px; fill: none; stroke: var(--text-soft); stroke-width: 1.4; }
</style>
</head>
<body>
<div class="canvas">
  <section class="card card--front">
    <div class="front-frame">
      <span class="front-square"></span>
      <div class="front-brand">Vela Stewardship</div>
    </div>
  </section>

  <section class="card card--back">
    <div class="back-panel"></div>
    <div class="back-info">
      <div class="brand-row">
        <span class="brand-square"></span>
        <span class="brand-name">Vela Stewardship</span>
      </div>
      <div class="person-name">Mara Dobrinsky</div>
      <p class="address">214/53 Penrose Street,<br>Port Ellery 3215</p>
      <ul class="contacts">
        <li>
          <svg viewBox="0 0 10 10"><path d="M2 1 L4 1 L4.5 3 L3.3 4 Q4.5 6 6 6.7 L7 5.5 L9 6 L9 8 Q5 9 2 5 Q1 3 2 1 Z" fill="#e4eef7" stroke="none"/></svg>
          <span>0458 317 642</span>
        </li>
        <li>
          <svg viewBox="0 0 10 10"><rect x="1" y="2.5" width="8" height="5.5"/><path d="M1 2.5 L5 5.5 L9 2.5"/></svg>
          <span>mara@velastewardship.com.au</span>
        </li>
        <li>
          <svg viewBox="0 0 10 10"><circle cx="5" cy="5" r="4"/><ellipse cx="5" cy="5" rx="1.8" ry="4"/><path d="M1 5 H9"/></svg>
          <span>www.velastewardship.com.au</span>
        </li>
      </ul>
    </div>
  </section>
</div>
</body>
</html>
```